Where Quiet Rivers Carry Us

I have a previously designed book cover, and although I am mostly happy with it, I do not care for the photo on the cover of the book. I would like to keep the fonts and scrollwork on the current book cover (the brown outer edge is optional).
I prefer a Christian focus with a soft, gentle, grieving, trusting feeling of a mother as God leads without the typical religious symbols (ie: huge hands, overwhelming crosses, Heaven opening). Softly toned or small Christian icons would be acceptable.
The book dimensions are 5.5 X 8.5 and the spine is 1/2" thick.
Original book cover is here: http://wherequietriverscarryus.pinebrookpages.net/p/free-books.html
Back cover book description (two photos and the logo for the back cover can be found below) :
For I am the Lord your God who takes hold of your right hand and says to you, "Do not fear, I will help you." Isaiah 41:13
One day you were here, Colby, the next you were at the throne of God. How I long to know what heaven is like so I can envision where you are. Are you talking to Gideon about the battles of old? Are you asking Paul about the stonings, the scales, and the shipwrecks? Or are you still just standing in awe of the God and Savior that your mother could never have come close to describing to you? How I long to stand in awe with you, praising the God who gives and takes away. Just like I told you all those times when you were here with us, "If you go first, I'll see you when I get there, my son." Love you, Mom
On Friday, February 18, 2011, God did the unthinkable in our lives: He chose to take our 12-year-old son, Colby, home to heaven in a skiing accident. It is only considered the unthinkable because our plans are not God's plans and our ways are not God's ways. Follow along on my journey through the valley of the shadow of death as my Savior, Jesus Christ, leads me.
(Author info)
Janna L. Voskuilen lives on a small farm in northern Wisconsin with her husband, Dale, and their children. Experiencing the tragic death of her son has caused her to draw closer to God as He leads her down an unexpected path to know Him better.
I have updated the back cover details to include the exact words for the back cover as well as two photos and a logo. Thank you, designers, for sharing your creativity!
Reason: Still looking for the perfect book cover!
Reason: Still looking for the perfect design!
Working on final revisions!

```html
<!DOCTYPE html>
<html lang="en">
<head>
<meta charset="utf-8">
<title>Where Quiet Rivers Carry Us — Cover Spread</title>
<link rel="stylesheet" href="https://fonts.googleapis.com/css2?family=Pinyon+Script&family=Arimo:wght@400&family=Cinzel:wght@400&display=swap">
<style>
  :root {
    --ink-dark: #0d0b0a;
    --spine: #141211;
    --back-deep: #2a221d;
    --back-mid: #5a4a3f;
    --back-light: #9c8878;
    --front-deep: #2b231e;
    --front-mid: #6b5a4e;
    --front-light: #b3a496;
    --text-soft: #ece7e1;
    --title-silver: #d8d4d0;
    --frame-white: #f4f2ef;
    --badge-grey: #cfcfcf;
  }
  * { margin: 0; padding: 0; box-sizing: border-box; }
  html, body { width: 1200px; height: 887px; overflow: hidden; background: var(--ink-dark); }
  .spread { position: relative; width: 1200px; height: 887px; overflow: hidden; }

  /* Back cover */
  .back-cover { position: absolute; left: 0; top: 0; width: 560px; height: 887px; }
  .back-photo {
    position: absolute; inset: 0;
    background:
      linear-gradient(90deg, transparent 0 41%, rgba(235,225,210,.35) 41% 44%, transparent 44%),
      linear-gradient(180deg, transparent 0 42%, rgba(235,225,210,.3) 42% 45%, transparent 45%),
      radial-gradient(ellipse at 42% 40%, var(--back-light) 0%, var(--back-mid) 40%, var(--back-deep) 90%);
  }
  .back-copy {
    position: absolute; left: 32px; top: 152px; width: 528px;
    font-family: "Arimo", Arial, sans-serif; font-size: 13.6px; line-height: 20.6px;
    color: var(--text-soft);
  }
  .back-copy p + p { margin-top: 20px; }

  .imprint {
    position: absolute; left: 32px; top: 565px; width: 134px; height: 67px;
    background: var(--badge-grey); border: 2px solid var(--frame-white);
    display: flex; align-items: center; justify-content: center; text-align: center;
    font-family: "Arimo", Arial, sans-serif; font-size: 14px; line-height: 17px;
    color: var(--ink-dark);
  }
  .author-portrait {
    position: absolute; left: 32px; top: 640px; width: 134px; height: 180px;
    border: 5px solid var(--frame-white);
    background: linear-gradient(160deg, #8a7a6c, #4a3d34);
  }
  .about-author {
    position: absolute; left: 188px; top: 573px; width: 345px;
    font-family: "Arimo", Arial, sans-serif; color: var(--text-soft);
  }
  .about-author h2 { font-weight: 400; font-size: 16px; letter-spacing: .3px; margin-bottom: 11px; }
  .about-author p { font-size: 13.6px; line-height: 20.6px; }

  /* Spine */
  .spine {
    position: absolute; left: 560px; top: 0; width: 82px; height: 887px;
    background: var(--spine);
  }
  .spine-title {
    position: absolute; left: 16px; top: 80px;
    writing-mode: vertical-rl;
    font-family: "Pinyon Script", cursive; font-size: 34px; color: var(--title-silver);
    white-space: nowrap;
  }
  .spine-author {
    position: absolute; left: 22px; top: 548px;
    writing-mode: vertical-rl;
    font-family: "Cinzel", serif; font-size: 27px; color: var(--frame-white);
    white-space: nowrap; letter-spacing: .5px;
  }

  /* Front cover */
  .front-cover { position: absolute; left: 642px; top: 0; width: 558px; height: 887px; }
  .front-photo {
    position: absolute; inset: 0;
    background:
      radial-gradient(ellipse at 70% 58%, var(--front-light) 0%, transparent 38%),
      radial-gradient(ellipse at 75% 15%, #8d7d70 0%, transparent 40%),
      linear-gradient(180deg, var(--front-mid) 0%, var(--front-deep) 100%);
  }
  .front-title {
    position: absolute; left: 40px; top: 44px; width: 500px;
    font-family: "Pinyon Script", cursive; font-weight: 400;
    font-size: 60px; line-height: 76px; color: var(--title-silver);
    text-shadow: 0 1px 2px rgba(0,0,0,.4);
  }
  .front-title .line-two { display: block; padding-left: 112px; }
  .front-author {
    position: absolute; left: 0; bottom: 12px; width: 558px; text-align: center;
    font-family: "Cinzel", serif; font-size: 38px; color: var(--frame-white);
    letter-spacing: .5px;
  }
</style>
</head>
<body>
<main class="spread">
  <section class="back-cover">
    <div class="back-photo" role="img" aria-label="Soft-focus church interior with wooden pews and a glowing cross of light on the far wall"></div>
    <div class="back-copy">
      <p>For I am the Lord your God who takes hold of your right and and says to you, "Do not fear, I will help you." Isaiah 41:13</p>
      <p>One day you were here, Colby, the next you were at the throne of God. How I long to know what heaven is like so I can envision where you are. Are you talking to Gideon about the battles of old? Are you asking Paul about the stonings, the scales, and the shipwrecks? Or are you still just standing in awe of the God and Savior that your mother could never have come close to describing to you? How I long to stand in awe with you, praising the God who gives and takes away. Just like I told you all those times when you were here with us, "If you go first, I'll see you when I get there, my son." Love you, Mom</p>
      <p>On Friday, February 18, 2011, God did the unthinkable in our lives: He chose to take our 12-year-old son, Colby, home to heaven in a skiing accident. It is only considered the unthinkable because our plans are not God's plans and our ways are not God's ways. Follow along on my journey through the valley of the shadow of death as my Savior, Jesus Christ, leads me.</p>
    </div>
    <div class="imprint">STILLWATER<br>MINISTRIES</div>
    <div class="author-portrait" role="img" aria-label="Portrait of the author in a plaid shirt and hat"></div>
    <div class="about-author">
      <h2>ABOUT THE AUTHOR</h2>
      <p>Janna L. Voskuilen lives on a small farm in northern Wisconsin with her husband, Dale, and their children. Experiencing the tragic death of her son has caused her to draw closer to God as He leads her down an unexpected path to know Him better.</p>
    </div>
  </section>

  <section class="spine">
    <div class="spine-title">Where Quiet Rivers Carry Us</div>
    <div class="spine-author">JANNA L. VOSKUILEN</div>
  </section>

  <section class="front-cover">
    <div class="front-photo" role="img" aria-label="Sepia photograph of a smiling boy in a backwards cap behind two clasped hands"></div>
    <h1 class="front-title">Where Quiet Rivers<span class="line-two">Carry Us</span></h1>
    <div class="front-author">JANNA L. VOSKUILEN</div>
  </section>
</main>
</body>
</html>
```